Malu Suds (Modern, Upscale, Organic Coffee Soap Packaging)

We need a new packaging design for a Hawaii-based, organic soap company called "Malu Suds" ('Malu' means 'Coffee' in the Hawaiian Language). Our eco-conscious mission is to 'upcycle' brewed coffee grounds from local coffee shops and cafes and transform them into high-quality soap and scrub products.For greater reference, please check out our main marketing platform - Instagram (@malusuds).We currently package our soaps in recycled paper envelopes (as demonstrated on our Instagram page and the attached file). While our customers really enjoy modern yet rustic aesthetic of the paper envelope, our issue is that consumers can't see or really smell the soaps without removing them from the packaging.

Target Market(s)

Millenials, People from Hawaii, People from Japan (one of Hawaii's biggest tourist markets)

Industry/Entity Type

Beauty

Font styles to use
Sans Serif

Colors

Designer to choose only greyscale colors for use in the design.

Requirements
Must have
• - must include/incorporate our original logo
• - must keep with aesthetic displayed on our website and instagram
Nice to have
• - I would like to see something that really communicates our commitment to our social mission to help the environment
• - I would like to see elegant, minimalist design (white marble?)
• - A soap packaging that would feel at home in a modern luxury home (bauhaus?)
Should not have
• - should not have any colors other than white, black, or gray (possibly coffee brown okay)

```html
<!DOCTYPE html>
<html lang="en">
<head>
<meta charset="utf-8">
<title>Malu Suds – Soap Label</title>
<link href="https://fonts.googleapis.com/css2?family=Poppins:wght@300;700&family=Roboto+Condensed:wght@400;700&display=swap" rel="stylesheet">
<style>
  :root {
    --backdrop: #5b5b5d;
    --label: #ffffff;
    --ink: #0d0d0d;
  }
  * { margin: 0; padding: 0; box-sizing: border-box; }
  html, body {
    width: 1200px;
    height: 959px;
    overflow: hidden;
    background: var(--backdrop);
  }
  .canvas {
    position: relative;
    width: 1200px;
    height: 959px;
  }
  .label {
    position: absolute;
    left: 262px;
    top: 259px;
    width: 674px;
    height: 441px;
    background: var(--label);
    border-radius: 22px;
    color: var(--ink);
  }
  .brand-name {
    position: absolute;
    left: 129px;
    top: 110px;
    width: 419px;
    display: flex;
    justify-content: space-between;
    font-family: "Poppins", sans-serif;
    font-weight: 700;
    font-size: 124px;
    line-height: 124px;
  }
  .brand-descriptor {
    position: absolute;
    left: 0;
    width: 100%;
    top: 239px;
    text-align: center;
    font-family: "Poppins", sans-serif;
    font-weight: 300;
    font-size: 48px;
    line-height: 56px;
    letter-spacing: 6px;
  }
  .scent-band {
    position: absolute;
    left: 129px;
    top: 305px;
    width: 419px;
    height: 26px;
    border-top: 1.5px solid var(--ink);
    border-bottom: 1.5px solid var(--ink);
    text-align: center;
    font-family: "Roboto Condensed", sans-serif;
    font-weight: 700;
    font-size: 16px;
    line-height: 23px;
  }
  .website {
    position: absolute;
    left: 0;
    width: 100%;
    top: 366px;
    text-align: center;
    font-family: "Roboto Condensed", sans-serif;
    font-weight: 700;
    font-size: 20px;
  }
  .social {
    position: absolute;
    left: 0;
    width: 100%;
    top: 397px;
    display: flex;
    justify-content: center;
    align-items: center;
    gap: 5px;
    font-family: "Roboto Condensed", sans-serif;
    font-weight: 400;
    font-size: 16px;
  }
  .social-dot {
    width: 16px;
    height: 16px;
    border: 1.8px solid var(--ink);
    border-radius: 50%;
  }
</style>
</head>
<body>
  <div class="canvas">
    <div class="label">
      <div class="brand-name"><span>M</span><span>A</span><span>L</span><span>U</span></div>
      <div class="brand-descriptor">SOAP CO.</div>
      <div class="scent-band">Scent: Plumeria</div>
      <div class="website">www.MaluSuds.com</div>
      <div class="social"><span class="social-dot"></span><span>@malusuds</span></div>
    </div>
  </div>
</body>
</html>
```